Business Card Design needed for logo design project

This project is linked to http://gigs.plumbfolio.net/task.aspx?id=472918
Kestrel Dues Partners.

Our company needs a Business Card Design. Please refer to our original project in the link above.

We would like the size to be a typical rectangle, no rounded edges or atypical sizes that will be costly to print. Thanks!

Target Market(s)

Small business owners in the U.S.

Industry/Entity Type

Business

```html
<!DOCTYPE html>
<html lang="en">
<head>
<meta charset="utf-8">
<title>Kestrel Dues Partners — Business Card</title>
<link href="https://fonts.googleapis.com/css2?family=Source+Sans+3:wght@400;600&display=swap" rel="stylesheet">
<style>
  :root {
    --backdrop: #ececec;
    --card: #ffffff;
    --brand-blue: #2f5aa8;
    --ink: #1e1e1e;
    --ink-soft: #4a4a4a;
  }
  html, body {
    margin: 0;
    padding: 0;
    width: 1091px;
    height: 1200px;
    overflow: hidden;
    background: var(--backdrop);
    font-family: "Source Sans 3", "Helvetica Neue", Arial, sans-serif;
  }
  .stage {
    width: 1091px;
    height: 1200px;
    display: flex;
    align-items: center;
    justify-content: center;
  }
  .business-card {
    position: relative;
    width: 896px;
    height: 392px;
    background: var(--card);
    box-shadow: 0 2px 10px rgba(0, 0, 0, 0.08);
  }
  .brand {
    position: absolute;
    left: 60px;
    top: 62px;
    display: flex;
    align-items: center;
    gap: 36px;
  }
  .brand-square {
    width: 64px;
    height: 64px;
    background: var(--brand-blue);
  }
  .brand-name {
    margin: 0;
    font-size: 30px;
    font-weight: 400;
    line-height: 1.2;
    letter-spacing: 0.5px;
    text-transform: uppercase;
    color: var(--brand-blue);
  }
  .contact {
    position: absolute;
    left: 247px;
    top: 228px;
    color: var(--ink);
  }
  .contact-name {
    margin: 0;
    font-size: 21px;
    font-weight: 600;
    line-height: 1.1;
  }
  .contact-title {
    margin: 2px 0 0;
    font-size: 16px;
    line-height: 1.2;
    color: var(--ink-soft);
  }
  .contact-details {
    margin: 24px 0 0;
    font-size: 16px;
    line-height: 1.45;
    color: var(--ink-soft);
  }
</style>
</head>
<body>
  <main class="stage">
    <article class="business-card">
      <header class="brand">
        <span class="brand-square" aria-hidden="true"></span>
        <h1 class="brand-name">Kestrel Dues<br>Partners</h1>
      </header>
      <section class="contact">
        <p class="contact-name">prename name</p>
        <p class="contact-title">professional job title</p>
        <p class="contact-details">
          email: name.name@kestrelmail.com<br>
          mobile: 01234 567 890
        </p>
      </section>
    </article>
  </main>
</body>
</html>
```